Brochure Design Project

We need a design for a company based in kingdom of saudi arabia, which is an event management company called lumevara...the design must match the logo and should be very creatuve,,

What We Serve
We conceptualize and implement events and campaigns of all sizes and calibres. As experts in our industry, we maintain national strategic relationships and an extensive knowledge base that allow us the resources to execute events at any level. Our understanding of customer service and commitment gives us a significant advantage above the rest. We are very flexible with the services that we offer and can offer our complete list of services in coordinating your requirements.
Our Services are designed to allow you to choose how best we can help to stage your occasion from conception to completion.
We aim to listen to your needs to match them to our services is what makes us strong.

Our Speciality
• Event Management Services
• Corporate Meetings & Conferences
• Corporate Training Programs
• Grand Openings
• Event Theme & Decor Styling
• Product Launch & Brand Awareness
• Lavish Social Events & Gala Dinners
• Marketing & PR Campaigns
Updates

HI

Please note that I will give high preference to 3d designs

dear all

thanks for the hard work....please try to show me designs with a balck base as well

Target Market(s)

hotels, automotive industries, resturants and etc

Industry/Entity Type

Events

Requirements
Must have
• the logo matching theme
Nice to have
• attached is my logo of lumevara and samples of brchures
Should not have
• less then 5 pages

```html
<!DOCTYPE html>
<html lang="en">
<head>
<meta charset="UTF-8">
<title>Lumevara Brochure Cover</title>
<link rel="stylesheet" href="https://fonts.googleapis.com/css2?family=Lato:wght@300&display=swap">
<style>
  :root {
    --teal: #0f9196;
    --olive: #a09614;
    --green: #79c832;
    --sage: #a0cb4a;
    --citron: #c8e128;
    --mint: #3de3a8;
    --lime: #b3eb55;
    --black: #000000;
    --white: #ffffff;
  }
  html, body {
    margin: 0;
    padding: 0;
    overflow: hidden;
    background: var(--black);
  }
  .cover {
    width: 900px;
    height: 1200px;
    display: grid;
    grid-template-columns: repeat(6, 150px);
    grid-template-rows: repeat(8, 150px);
    overflow: hidden;
  }
  .tile { display: block; }
  .teal { background: var(--teal); }
  .olive { background: var(--olive); }
  .green { background: var(--green); }
  .sage { background: var(--sage); }
  .citron { background: var(--citron); }
  .mint { background: var(--mint); }
  .lime { background: var(--lime); }

  .brand-panel {
    grid-column: 1 / 5;
    grid-row: 5 / 8;
    background: var(--black);
    position: relative;
  }
  .brand-name {
    position: absolute;
    left: 130px;
    top: 305px;
    margin: 0;
    font-family: "Lato", sans-serif;
    font-weight: 300;
    font-size: 56px;
    letter-spacing: 9px;
    line-height: 1;
    color: var(--white);
    text-transform: uppercase;
  }
</style>
</head>
<body>
<main class="cover">
  <!-- row 1 -->
  <div class="tile teal" style="grid-column:1;grid-row:1"></div>
  <div class="tile olive" style="grid-column:2;grid-row:1"></div>
  <div class="tile green" style="grid-column:3;grid-row:1"></div>
  <div class="tile sage" style="grid-column:4;grid-row:1"></div>
  <div class="tile green" style="grid-column:5;grid-row:1"></div>
  <div class="tile citron" style="grid-column:6;grid-row:1"></div>
  <!-- row 2 -->
  <div class="tile citron" style="grid-column:1 / 3;grid-row:2"></div>
  <div class="tile mint" style="grid-column:3;grid-row:2 / 4"></div>
  <div class="tile green" style="grid-column:4;grid-row:2"></div>
  <div class="tile mint" style="grid-column:5;grid-row:2"></div>
  <div class="tile green" style="grid-column:6;grid-row:2"></div>
  <!-- row 3 -->
  <div class="tile lime" style="grid-column:1;grid-row:3"></div>
  <div class="tile olive" style="grid-column:2;grid-row:3"></div>
  <div class="tile lime" style="grid-column:4;grid-row:3"></div>
  <div class="tile citron" style="grid-column:5;grid-row:3 / 5"></div>
  <div class="tile teal" style="grid-column:6;grid-row:3"></div>
  <!-- row 4 -->
  <div class="tile teal" style="grid-column:1;grid-row:4"></div>
  <div class="tile sage" style="grid-column:2;grid-row:4"></div>
  <div class="tile sage" style="grid-column:3;grid-row:4"></div>
  <div class="tile green" style="grid-column:4;grid-row:4"></div>
  <div class="tile green" style="grid-column:6;grid-row:4 / 6"></div>
  <!-- brand panel -->
  <section class="brand-panel">
    <h1 class="brand-name">Lumevara</h1>
  </section>
  <!-- right column beside panel -->
  <div class="tile teal" style="grid-column:5;grid-row:5"></div>
  <div class="tile olive" style="grid-column:5 / 7;grid-row:6"></div>
  <div class="tile mint" style="grid-column:5;grid-row:7"></div>
  <div class="tile citron" style="grid-column:6;grid-row:7"></div>
  <!-- bottom row -->
  <div class="tile olive" style="grid-column:1;grid-row:8"></div>
  <div class="tile green" style="grid-column:2;grid-row:8"></div>
  <div class="tile sage" style="grid-column:3;grid-row:8"></div>
  <div class="tile teal" style="grid-column:4;grid-row:8"></div>
  <div class="tile green" style="grid-column:5 / 7;grid-row:8"></div>
</main>
</body>
</html>
```